Norvale Rentals and Supply Flyer

A4 flyer to send electronic to potential customer via email to tell them about Norvale Rentals.
We are start up company looking at sending companies a flyer to introduce the business.

No Folds required - just a standard A4 design

Target Market(s)

Concrete and construction companies

Industry/Entity Type

Construction Company

Font styles to use
Sans Serif

Colors
fbee3e

Requirements
Must have
• Norvale Logo
• Images provided
Nice to have
• Black and Yellow colour scheme
Should not have
• n/a

```html
<!DOCTYPE html>
<html lang="en">
<head>
<meta charset="utf-8">
<title>Norvale Rentals and Supply Flyer</title>
<link href="https://fonts.googleapis.com/css2?family=Bebas+Neue&family=Montserrat:wght@400;600;700;800&display=swap" rel="stylesheet">
<style>
  :root {
    --yellow: #fbd21e;
    --ink: #161616;
    --panel: #222222;
    --white: #ffffff;
    --muted: #d9d9d9;
    --stage: #e4e4e4;
  }
  * { box-sizing: border-box; margin: 0; padding: 0; }
  html, body { width: 1200px; height: 986px; overflow: hidden; background: var(--stage); }
  body { font-family: "Montserrat", sans-serif; }

  .flyer {
    position: absolute; left: 267px; top: 23px; width: 665px; height: 940px;
    background: radial-gradient(ellipse at 55% 40%, #3a3a3a 0%, #1f1f1f 55%, var(--ink) 100%);
    overflow: hidden; color: var(--white);
    box-shadow: 0 6px 24px rgba(0,0,0,.25);
  }

  .brand { position: absolute; left: 40px; top: 38px; display: flex; align-items: center; gap: 8px; }
  .brand-mark { width: 22px; height: 22px; background: var(--yellow); }
  .brand-name { font-weight: 800; font-size: 18px; color: var(--yellow); letter-spacing: .5px; text-transform: uppercase; }

  .headline { position: absolute; left: 40px; top: 86px; width: 340px; font-family: "Bebas Neue", sans-serif; font-weight: 400; line-height: .95; }
  .headline-primary { display: block; font-size: 58px; color: var(--yellow); white-space: nowrap; }
  .headline-secondary { display: block; font-size: 58px; color: var(--white); white-space: nowrap; }
  .tagline-sub { position: absolute; left: 42px; top: 212px; width: 330px; font-size: 12.5px; font-weight: 700; line-height: 1.25; }

  .photo { position: absolute; }
  .photo-vacuum { left: 400px; top: 30px; width: 225px; height: 370px; z-index: 2;
    background: linear-gradient(170deg, #f07a2a 0%, #d9621b 45%, #2a2a2a 100%); border-radius: 10px 10px 4px 4px; }
  .photo-grinder { left: 165px; top: 300px; width: 225px; height: 200px; z-index: 2;
    background: linear-gradient(160deg, #f1f1f1 0%, #b9bcc0 55%, #55585c 100%); border-radius: 8px; }

  .yellow-panel { position: absolute; left: 430px; top: 250px; width: 235px; height: 330px; background: var(--yellow); }

  .services { position: absolute; left: 58px; top: 282px; list-style: none; }
  .service { width: 80px; height: 80px; text-align: center; }
  .service-icon { display: block; margin: 0 auto; width: 44px; height: 44px; border: 2px solid var(--yellow); border-radius: 50%; position: relative; }
  .service-icon::after { content: ""; position: absolute; left: 12px; top: 19px; width: 16px; height: 2px; background: var(--white); }
  .service-label { display: block; margin-top: 6px; font-size: 11px; color: var(--white); }

  .suppliers { position: absolute; left: 452px; top: 440px; }
  .suppliers-title { font-weight: 800; font-size: 16px; color: var(--ink); text-transform: uppercase; margin-bottom: 10px; }
  .supplier-grid { display: grid; grid-template-columns: 90px 90px; gap: 10px; }
  .supplier-badge { height: 36px; background: var(--white); }

  .follow { position: absolute; left: 446px; top: 602px; width: 200px; }
  .follow-title { font-weight: 800; font-size: 13px; text-transform: uppercase; }
  .social { display: flex; gap: 8px; margin-top: 8px; }
  .social-icon { width: 24px; height: 24px; background: var(--white); border-radius: 4px; }
  .contact { list-style: none; margin-top: 12px; font-size: 10px; line-height: 1.45; }
  .contact li { display: flex; align-items: flex-start; gap: 7px; margin-bottom: 5px; }
  .contact svg { width: 11px; height: 11px; flex: none; margin-top: 2px; }

  .benefits { position: absolute; left: 60px; top: 700px; width: 350px; list-style: none; }
  .benefit { display: flex; gap: 10px; font-size: 11px; line-height: 1.35; margin-bottom: 10px; }
  .benefit svg { flex: none; width: 14px; height: 14px; margin-top: 2px; }

  .promise { position: absolute; left: 60px; top: 798px; font-size: 21px; line-height: 1.25; color: var(--yellow); }
  .cta { position: absolute; left: 60px; top: 856px; font-size: 18px; font-weight: 800; line-height: 1.2; }

  .phone-band { position: absolute; left: 40px; right: 40px; top: 886px; height: 46px; background: var(--yellow);
    display: flex; align-items: center; gap: 12px; padding-left: 22px; }
  .phone-band svg { width: 24px; height: 24px; }
  .phone-number { font-family: "Montserrat", sans-serif; font-weight: 800; font-size: 34px; color: var(--ink); letter-spacing: 1px; }
</style>
</head>
<body>
<main class="flyer">
  <div class="brand"><span class="brand-mark"></span><span class="brand-name">Norvale Rentals</span></div>

  <h1 class="headline">
    <span class="headline-primary">Norvale Rentals</span>
    <span class="headline-secondary">And Supply</span>
  </h1>
  <p class="tagline-sub">Concrete, Construction and Communication Hire Equipment</p>

  <div class="yellow-panel"></div>
  <div class="photo photo-vacuum" role="img" aria-label="Orange industrial dust extractor vacuum with hose and wand"></div>
  <div class="photo photo-grinder" role="img" aria-label="Floor grinding machine with water tank and grey base"></div>

  <ul class="services">
    <li class="service"><span class="service-icon"></span><span class="service-label">Honing</span></li>
    <li class="service"><span class="service-icon"></span><span class="service-label">Polishing</span></li>
    <li class="service"><span class="service-icon"></span><span class="service-label">Cutting</span></li>
    <li class="service"><span class="service-icon"></span><span class="service-label">Drilling</span></li>
    <li class="service"><span class="service-icon"></span><span class="service-label">Demolation</span></li>
  </ul>

  <section class="suppliers">
    <h2 class="suppliers-title">Our Suppliers</h2>
    <div class="supplier-grid">
      <div class="supplier-badge"></div><div class="supplier-badge"></div>
      <div class="supplier-badge"></div><div class="supplier-badge"></div>
    </div>
  </section>

  <section class="follow">
    <h2 class="follow-title">Follow us on</h2>
    <div class="social"><span class="social-icon"></span><span class="social-icon"></span></div>
    <ul class="contact">
      <li><svg viewBox="0 0 12 12"><circle cx="6" cy="6" r="5" fill="none" stroke="var(--yellow)" stroke-width="1.6"/></svg><span>www.norvalerentals.example</span></li>
      <li><svg viewBox="0 0 12 12"><rect x="1" y="2.5" width="10" height="7" fill="none" stroke="var(--yellow)" stroke-width="1.4"/><path d="M1 3l5 4 5-4" fill="none" stroke="var(--yellow)" stroke-width="1.2"/></svg><span>info@norvalerentals.example</span></li>
      <li><svg viewBox="0 0 12 12"><path d="M6 11S2 6.8 2 4.5a4 4 0 018 0C10 6.8 6 11 6 11z" fill="var(--yellow)"/><circle cx="6" cy="4.5" r="1.4" fill="var(--ink)"/></svg><span>unit 4, 12 Foundry Way<br>Kelmore 6099</span></li>
    </ul>
  </section>

  <ul class="benefits">
    <li class="benefit"><svg viewBox="0 0 14 14"><circle cx="7" cy="7" r="7" fill="var(--yellow)"/><path d="M4 7.2l2 2 4-4.2" fill="none" stroke="var(--ink)" stroke-width="1.6"/></svg><span>Diamond Consumable for sale- core barrels,diamond segments and specialized tooling</span></li>
    <li class="benefit"><svg viewBox="0 0 14 14"><circle cx="7" cy="7" r="7" fill="var(--yellow)"/><path d="M4 7.2l2 2 4-4.2" fill="none" stroke="var(--ink)" stroke-width="1.6"/></svg><span>Good old fashion customer service with over 15 year's experience in the concrete and construction industry.</span></li>
  </ul>

  <p class="promise">We will BEAT any written<br>quote from our competitors.</p>
  <p class="cta">Call us Now</p>

  <div class="phone-band">
    <svg viewBox="0 0 24 24"><path d="M6.6 10.8a15 15 0 006.6 6.6l2.2-2.2a1 1 0 011-.25 11.4 11.4 0 003.6.57 1 1 0 011 1V20a1 1 0 01-1 1A17 17 0 013 4a1 1 0 011-1h3.5a1 1 0 011 1c0 1.25.2 2.45.57 3.57a1 1 0 01-.25 1z" fill="var(--white)"/></svg>
    <span class="phone-number">0400 555 318</span>
  </div>
</main>
</body>
</html>
```